High-end Oceanfront Real Estate Group Needs Clean, Modern Web Design

I’m looking for a clean, professional, modern and beautiful homepage web design for a Real Estate group in Southern California, USA.

The group/company is “Marlow on the Shore,” and they specialize in high end (i.e. expensive), oceanfront real estate in the Orange County area.

The look and feel of the page should accentuate the brand qualities: luxurious/expensive, professional, and beautiful (Orange County is one of the most beautiful areas in all the US and we would love the site to emphasize the beautiful beaches and scenery it has to offer).

Looks we like:
• www.brantleyhomesrealty.example
• www.keptbyfenwick.example -- I think the design is pretty out-dated in this site, but I like the organization/layout of the site

Header Tags (I don’t know if we can fit all of these, may need a side-menu, but I’d prefer header title only if possible):
• Welcome
• Featured Listings
• Previously Sold
• Sell
• Property Search
• Team
• Videos
• Blog
• Explore O.C.
• Contact

I have attached the beach and logo pics that we would like to use as the header, a few pictures of the team, and one sample home/view pic which can be used in any of the other sections (for pictures of the homes, just find expensive oceanfront houses and that will be fine).

I promise to provide feedback to each and every design submission. I appreciate the hard work that all of you are putting into your designs. There can be only one contest winner, but I hope to give all of you helpful feedback to submit the best designs possible!

Target Market(s)

Very wealthy home owners of oceanfront properties. These properties are worth several millions of dollars, and thus the site and brand needs to be targeted to very wealthy, successful individuals and families (both US and international buyers).

Industry/Entity Type

Real Estate

Number of Pages Required

2 page

Requirements
Must have
• I don’t want to give too many requirements, because I want to let you all be creative. However, here are the few Must Haves:
• Must submit 2 page designs (a home page and a sub page)
• Must use logo provided
• Focus is mostly on homes, but I would like to include some beach/ocean imagery as well
• The first “item” on the home page should be an accordion/slider which shows pictures of homes and with 1 line of text: “List with the Leader” and two link buttons: “Sell Your Home” and “Buy Your Home”
• Color palette needs to be mainly blues--to match ocean and sky blue
• Exported in all major formats (psd,ai,eps,png,jpeg,etc)
Nice to have
• We don’t necessarily need all of these, but would like to feature most:
• List of videos
• “Meet the Team”—brief team bios and pics
• Link(s) to Blog
• “List with the Leader” – section on why they should choose this firm
• Featured Listings
• Previously Sold

```html
<!DOCTYPE html>
<html lang="en">
<head>
<meta charset="utf-8">
<title>Marlow on the Shore — Oceanfront Real Estate</title>
<link rel="stylesheet" href="https://fonts.googleapis.com/css2?family=Open+Sans:wght@300;400;600;700&family=Arimo:wght@400;700&display=swap">
<style>
:root{
  --night:#0d1826;
  --nav:#1a2230;
  --navy:#0f1c2b;
  --tab-active:#2a4a6e;
  --paper:#eeeeee;
  --white:#ffffff;
  --ink:#2b2b2b;
  --link:#1d4f7a;
  --foot:#222222;
  --foot-bottom:#111111;
  --logo-box:#d8d8d6;
  --logo-ink:#4a4a4a;
}
*{box-sizing:border-box;margin:0;padding:0}
html,body{width:1200px;height:2909px;overflow:hidden}
body{position:relative;font-family:"Open Sans",Arial,sans-serif;color:var(--ink);background:var(--white)}

/* hero */
.hero{position:absolute;left:0;top:0;width:1200px;height:564px;overflow:hidden}
.hero-photo{position:absolute;inset:0;background:linear-gradient(180deg,#2b3444 0%,#1d2533 45%,#3b3d40 78%,#23272c 100%)}
.hero-links{position:absolute;inset:0}
.hero-icon{position:absolute;width:78px;height:78px;border-radius:50%;background:var(--white);border:3px solid #1b1b1b;box-shadow:0 0 0 2px rgba(255,255,255,.6)}
.hero-icon svg{width:100%;height:100%}
.hero-label{position:absolute;color:var(--white);font-weight:700;font-size:20px;white-space:nowrap}
.brand-box{position:absolute;background:var(--logo-box);display:flex;flex-direction:column;align-items:center;justify-content:center;color:var(--logo-ink);font-weight:300;text-transform:uppercase;line-height:1}
.hero .brand-box{left:480px;top:191px;width:232px;height:161px}
.hero .brand-box .b1{font-size:46px;letter-spacing:2px}
.hero .brand-box .b2{font-size:20px;letter-spacing:6px;margin-top:10px}

/* nav */
.topnav{position:absolute;left:0;top:564px;width:1200px;height:111px;background:var(--nav)}
.topnav .brand-box{left:132px;top:4px;width:154px;height:107px}
.topnav .brand-box .b1{font-size:32px;letter-spacing:1px}
.topnav .brand-box .b2{font-size:13px;letter-spacing:4px;margin-top:8px}
.menu{position:absolute;left:339px;top:70px;display:flex;height:41px}
.menu a{color:#e6e6e6;text-decoration:none;font-size:14px;line-height:41px;padding:0 20px;white-space:nowrap}
.menu a.current{background:#d7d7d7;color:#333}
.social{position:absolute;display:flex;gap:8px}
.social span{display:block;width:31px;height:31px;border-radius:50%;border:1.5px solid #cfcfcf;position:relative}
.social span::after{content:"";position:absolute;left:50%;top:50%;width:9px;height:9px;margin:-4.5px 0 0 -4.5px;border-radius:50%;background:#cfcfcf}
.topnav .social{left:825px;top:21px}
.lang{position:absolute;left:986px;top:20px;width:80px;height:32px;border:1.5px solid #cfcfcf;border-radius:16px;color:#e6e6e6;font-size:12px;line-height:29px;padding-left:12px}
.lang::after{content:"";position:absolute;right:10px;top:11px;width:6px;height:6px;border-right:1.5px solid #ddd;border-bottom:1.5px solid #ddd;transform:rotate(45deg)}

/* welcome */
.welcome{position:absolute;left:0;top:675px;width:1200px;height:302px;background:var(--paper);text-align:center}
.welcome h1{position:absolute;left:0;right:0;top:43px;font-weight:300;font-size:37px;color:#333;letter-spacing:.5px}
.welcome h1 span{color:#777}
.welcome .rule{position:absolute;left:423px;top:98px;width:354px;height:1px;background:#bdbdbd}
.welcome .rule::after{content:"";position:absolute;left:160px;top:-1px;width:34px;height:3px;background:#777}
.welcome .tag{position:absolute;left:0;right:0;top:112px;font-size:15px;letter-spacing:5px;color:#777}
.welcome p{position:absolute;left:141px;top:152px;width:919px;font-size:13.4px;line-height:21px;color:#555}

/* listings */
.listings{position:absolute;left:0;top:977px;width:1200px;height:689px;background:var(--navy)}
.filter{position:absolute;left:368px;top:46px;display:flex;border:1.5px solid #9aa3ad;border-radius:5px;overflow:hidden}
.filter span{color:#e6e6e6;font-size:13px;line-height:40px;text-align:center;border-left:1.5px solid #9aa3ad}
.filter span:first-child{border-left:0;background:var(--tab-active)}
.card{position:absolute;width:213px;height:227px;background:var(--white);border-bottom:3px solid #6f8fb0}
.card .photo{height:148px}
.card h3{font-weight:400;font-size:13px;color:#222;padding:6px 6px 0}
.card .where{font-size:10px;color:#555;padding:4px 6px 0;display:flex;align-items:center;gap:4px}
.card .where svg{width:9px;height:12px}
.card .blurb{font-size:10px;color:#555;padding-top:6px;border-top:1px solid #e2e2e2;margin:5px 6px 0}

/* blog */
.blog{position:absolute;left:0;top:1666px;width:1200px;height:459px;background:linear-gradient(135deg,#e6e6e6 0%,#f3f3f3 35%,#e2e2e2 65%,#efefef 100%)}
.blog h2,.team h2{position:absolute;left:0;right:0;text-align:center;font-weight:700;color:#2b2b2b}
.blog h2{top:28px;font-size:29px}
.blog .bar{position:absolute;left:520px;top:73px;width:160px;height:2px;background:#1b1b1b}
.post{position:absolute;width:445px;height:100px;font-family:"Arimo",Arial,sans-serif}
.post .thumb{position:absolute;top:0;width:107px;height:88px}
.post h4{position:absolute;top:0;font-size:13px;font-weight:700;color:var(--link);text-decoration:underline;white-space:nowrap}
.post time{position:absolute;top:25px;font-size:12px;font-weight:700;color:#222}
.post p{position:absolute;top:43px;font-size:12px;line-height:16px;color:#444;width:250px}
.post.left .thumb{right:0}
.post.left h4{left:0}
.post.left time,.post.left p{right:122px;text-align:right}
.post.right .thumb{left:0}
.post.right h4,.post.right time,.post.right p{left:123px}
.blog .sep{position:absolute;height:1px;background:#c4c4c4}

/* team */
.team{position:absolute;left:0;top:2125px;width:1200px;height:462px;background:var(--white)}
.team h2{top:48px;font-size:27px}
.team .tree{position:absolute;left:0;top:0}
.member{position:absolute;text-align:center;width:160px}
.member .ring{margin:0 auto;border-radius:50%;border:1px solid #c9c9c9;display:flex;align-items:center;justify-content:center}
.member .face{border-radius:50%;background:linear-gradient(180deg,#c9cfd6,#7d8793)}
.member b{display:block;font-size:15px;margin-top:12px;color:#222}
.quote{position:absolute;left:152px;top:362px;width:893px;height:92px;border:1px solid #cfcfcf;padding:8px 12px 0 40px;font-size:12.6px;line-height:19px;color:#666}
.quote::before{content:"\201C";position:absolute;left:10px;top:-6px;font-size:48px;color:#999;font-family:Georgia,serif}
.quote .tip{position:absolute;left:110px;top:-22px;border-left:1px solid #cfcfcf;height:22px}
.quote .tip2{position:absolute;left:111px;top:-22px;width:31px;height:1px;background:#cfcfcf;transform-origin:0 0;transform:rotate(35deg)}

/* footer */
.footer{position:absolute;left:0;top:2587px;width:1200px;height:277px;background:var(--foot);color:#ddd}
.foot-links{position:absolute;left:132px;top:98px;display:flex;align-items:center;font-size:12px;color:#ddd}
.foot-links i{display:inline-block;width:5px;height:5px;background:#777;margin:0 11px}
.footer .hr{position:absolute;left:132px;top:140px;width:936px;height:1px;background:#3b3b3b}
.contact-card{position:absolute;left:132px;top:166px;font-size:12px;line-height:18px;color:#ccc}
.contact-card strong{display:block;font-size:15px;color:#fff;margin-bottom:4px}
.contact-lines{position:absolute;left:359px;top:168px;font-size:12px;color:#ccc}
.contact-lines div{display:flex;align-items:center;gap:12px;height:26px}
.contact-lines svg{width:14px;height:14px}
.signup-field{position:absolute;left:573px;top:166px;width:229px;height:36px;background:#111;border:1px solid #444;color:#ccc;font-size:12px;line-height:34px;padding-left:8px}
.signup-btn{position:absolute;left:573px;top:211px;width:229px;height:32px;background:linear-gradient(180deg,#e8e8e8,#9d9d9d);color:#fff;font-weight:700;font-size:14px;letter-spacing:2px;text-align:center;line-height:32px;border-radius:2px}
.footer .brand-box{left:923px;top:157px;width:143px;height:99px}
.footer .brand-box .b1{font-size:28px}
.footer .brand-box .b2{font-size:11px;letter-spacing:3px;margin-top:7px}
.legal{position:absolute;left:0;top:2864px;width:1200px;height:45px;background:var(--foot-bottom)}
.legal p{position:absolute;left:132px;top:14px;font-size:12px;color:#bbb}
.legal .social{left:925px;top:7px;gap:6px}
.legal .social span{background:#f2f2f2;border:0;width:30px;height:30px}
.legal .social span::after{background:#111}
</style>
</head>
<body>

<header class="hero">
  <div class="hero-photo" role="img" aria-label="Evening photograph of a modern oceanfront home with lit terraces and trees"></div>
  <svg class="hero-links" width="1200" height="564" viewBox="0 0 1200 564" fill="none" stroke="#e8e8e8" stroke-width="2" stroke-dasharray="3 5">
    <path d="M302 130 C330 200 420 230 480 240"/>
    <path d="M898 130 C870 200 780 230 712 240"/>
    <path d="M173 273 H480"/>
    <path d="M1022 273 H712"/>
    <path d="M293 425 C330 360 420 340 480 330"/>
    <path d="M893 412 C860 360 780 340 712 330"/>
  </svg>

  <div class="hero-icon" style="left:263px;top:52px"><svg viewBox="0 0 78 78"><circle cx="39" cy="39" r="32" fill="#1b1b1b"/><circle cx="34" cy="42" r="9" fill="none" stroke="#fff" stroke-width="5" stroke-dasharray="4 3"/><circle cx="34" cy="42" r="3" fill="#fff"/><circle cx="48" cy="28" r="6" fill="none" stroke="#fff" stroke-width="4" stroke-dasharray="3 2"/></svg></div>
  <div class="hero-label" style="left:216px;top:134px">Services</div>

  <div class="hero-icon" style="left:859px;top:52px"><svg viewBox="0 0 78 78"><circle cx="39" cy="39" r="32" fill="#1b1b1b"/><circle cx="35" cy="35" r="11" fill="none" stroke="#fff" stroke-width="5"/><path d="M43 43 L54 54" stroke="#fff" stroke-width="6" stroke-linecap="round"/></svg></div>
  <div class="hero-label" style="left:909px;top:142px">Property Search</div>

  <div class="hero-icon" style="left:95px;top:234px"><svg viewBox="0 0 78 78"><circle cx="39" cy="39" r="32" fill="#1b1b1b"/><rect x="21" y="27" width="36" height="24" rx="6" fill="#fff"/><path d="M35 33 L45 39 L35 45 Z" fill="#1b1b1b"/></svg></div>
  <div class="hero-label" style="left:95px;top:334px">Videos</div>

  <div class="hero-icon" style="left:1022px;top:234px"><svg viewBox="0 0 78 78"><circle cx="39" cy="39" r="32" fill="#1b1b1b"/><circle cx="28" cy="33" r="5" fill="#fff"/><circle cx="39" cy="30" r="6" fill="#fff"/><circle cx="50" cy="33" r="5" fill="#fff"/><path d="M19 50 C19 40 37 40 37 50 Z M41 50 C41 40 59 40 59 50 Z M28 48 C28 36 50 36 50 48 Z" fill="#fff"/></svg></div>
  <div class="hero-label" style="left:1040px;top:330px">Team</div>

  <div class="hero-icon" style="left:254px;top:425px"><svg viewBox="0 0 78 78"><circle cx="39" cy="39" r="32" fill="#1b1b1b"/><path d="M39 58 C30 46 27 40 27 33 A12 12 0 0 1 51 33 C51 40 48 46 39 58 Z" fill="#fff"/><circle cx="39" cy="33" r="4.5" fill="#1b1b1b"/></svg></div>
  <div class="hero-label" style="left:342px;top:486px">Contact US</div>

  <div class="hero-icon" style="left:854px;top:411px"><svg viewBox="0 0 78 78"><circle cx="39" cy="39" r="32" fill="#1b1b1b"/><path d="M22 28 H56 V48 H36 L28 55 V48 H22 Z" fill="#fff"/></svg></div>
  <div class="hero-label" style="left:786px;top:484px">Blog</div>

  <div class="brand-box"><span class="b1">Marlow</span><span class="b2">on the shore</span></div>
</header>

<nav class="topnav">
  <div class="brand-box"><span class="b1">Marlow</span><span class="b2">on the shore</span></div>
  <div class="social" aria-label="Social links"><span></span><span></span><span></span><span></span></div>
  <div class="lang">English</div>
  <div class="menu">
    <a class="current">Home</a><a>About us</a><a>Property Search</a><a>Team</a><a>Videos</a><a>Blog</a><a>Explore O.C</a><a>Contact</a>
  </div>
</nav>

<section class="welcome">
  <h1>WELCOME TO <span>MARLOW</span></h1>
  <div class="rule"></div>
  <div class="tag">ON THE SHORE</div>
  <p>Lorem ipsum dolor sit amet, consectetuer adipiscing elit, sed diam nonummy nibh euismod tincidunt ut laoreet dolore magna aliquam erat volutpat. Ut wisi enim ad minim veniam, quis nostrud exerci tation ullamcorper suscipit lobortis nisl ut aliquip ex ea commodo consequat. Duis autem vel eum iriure dolor in hendrerit in vulputate velit esse molestie consequat, vel illum dolore eu feugiat nulla facilisis at vero eros et accumsan et iusto odio dignissim qui blandit praesent luptatum zzril delenit augue duis dolore te feugait nulla facilisi.</p>
</section>

<section class="listings">
  <div class="filter">
    <span style="width:150px">Featured Listings</span><span style="width:152px">Previously Sold</span><span style="width:81px">Sell</span><span style="width:80px">All</span>
  </div>

  <article class="card" style="left:132px;top:132px"><div class="photo" role="img" aria-label="Bright white living room interior" style="background:linear-gradient(160deg,#f1ece4,#b9aa96 60%,#6d5a48)"></div><h3>Lorem ipsum dolor sit amet</h3><div class="where"><svg viewBox="0 0 9 12"><path d="M4.5 12 C1.5 8 0 6 0 4.5 A4.5 4.5 0 0 1 9 4.5 C9 6 7.5 8 4.5 12 Z" fill="#333"/></svg>5 Boroughs, New York, Ny</div><p class="blurb">It us a long established fact that a</p></article>
  <article class="card" style="left:370px;top:132px"><div class="photo" role="img" aria-label="Oceanfront villa with pool at sunset" style="background:linear-gradient(180deg,#3f78c8,#8fb3d9 45%,#2f4a3a 75%,#203028)"></div><h3>Lorem ipsum dolor sit amet</h3><div class="where"><svg viewBox="0 0 9 12"><path d="M4.5 12 C1.5 8 0 6 0 4.5 A4.5 4.5 0 0 1 9 4.5 C9 6 7.5 8 4.5 12 Z" fill="#333"/></svg>5 Boroughs, New York, Ny</div><p class="blurb">It us a long established fact that a</p></article>
  <article class="card" style="left:611px;top:132px"><div class="photo" role="img" aria-label="Lit modern home with pool at dusk" style="background:linear-gradient(180deg,#1f3f7a,#7a5a3a 55%,#2aa0c8 85%)"></div><h3>Lorem ipsum dolor sit amet</h3><div class="where"><svg viewBox="0 0 9 12"><path d="M4.5 12 C1.5 8 0 6 0 4.5 A4.5 4.5 0 0 1 9 4.5 C9 6 7.5 8 4.5 12 Z" fill="#333"/></svg>5 Boroughs, New York, Ny</div><p class="blurb">It us a long established fact that a</p></article>
  <article class="card" style="left:855px;top:132px"><div class="photo" role="img" aria-label="Beach house terrace over the ocean at twilight" style="background:linear-gradient(180deg,#5a6fb0,#b08aa8 45%,#2b4b6a 70%,#3a3024)"></div><h3>Lorem ipsum dolor sit amet</h3><div class="where"><svg viewBox="0 0 9 12"><path d="M4.5 12 C1.5 8 0 6 0 4.5 A4.5 4.5 0 0 1 9 4.5 C9 6 7.5 8 4.5 12 Z" fill="#333"/></svg>5 Boroughs, New York, Ny</div><p class="blurb">It us a long established fact that a</p></article>

  <article class="card" style="left:132px;top:387px"><div class="photo" role="img" aria-label="Living room with large windows" style="background:linear-gradient(170deg,#d8d2c8,#9c8f7e 55%,#5a4e44)"></div><h3>Lorem ipsum dolor sit amet</h3><div class="where"><svg viewBox="0 0 9 12"><path d="M4.5 12 C1.5 8 0 6 0 4.5 A4.5 4.5 0 0 1 9 4.5 C9 6 7.5 8 4.5 12 Z" fill="#333"/></svg>5 Boroughs, New York, Ny</div><p class="blurb">It us a long established fact that a</p></article>
  <article class="card" style="left:370px;top:387px"><div class="photo" role="img" aria-label="Modern home with blue pool in daylight" style="background:linear-gradient(180deg,#6fa2d8,#a88a6a 50%,#1f86c0 80%)"></div><h3>Lorem ipsum dolor sit amet</h3><div class="where"><svg viewBox="0 0 9 12"><path d="M4.5 12 C1.5 8 0 6 0 4.5 A4.5 4.5 0 0 1 9 4.5 C9 6 7.5 8 4.5 12 Z" fill="#333"/></svg>5 Boroughs, New York, Ny</div><p class="blurb">It us a long established fact that a</p></article>
  <article class="card" style="left:611px;top:387px"><div class="photo" role="img" aria-label="Warmly lit open-plan interior" style="background:linear-gradient(170deg,#7a3a2a,#b0684a 45%,#3a2a22)"></div><h3>Lorem ipsum dolor sit amet</h3><div class="where"><svg viewBox="0 0 9 12"><path d="M4.5 12 C1.5 8 0 6 0 4.5 A4.5 4.5 0 0 1 9 4.5 C9 6 7.5 8 4.5 12 Z" fill="#333"/></svg>5 Boroughs, New York, Ny</div><p class="blurb">It us a long established fact that a</p></article>
  <article class="card" style="left:855px;top:387px"><div class="photo" role="img" aria-label="Mediterranean-style mansion facade at dusk" style="background:linear-gradient(180deg,#2f4f8a,#c07a4a 50%,#6a3a28)"></div><h3>Lorem ipsum dolor sit amet</h3><div class="where"><svg viewBox="0 0 9 12"><path d="M4.5 12 C1.5 8 0 6 0 4.5 A4.5 4.5 0 0 1 9 4.5 C9 6 7.5 8 4.5 12 Z" fill="#333"/></svg>5 Boroughs, New York, Ny</div><p class="blurb">It us a long established fact that a</p></article>
</section>

<section class="blog">
  <h2>Latest Blog</h2>
  <div class="bar"></div>

  <article class="post left" style="left:132px;top:98px"><h4>Ut tellus dolor, dapibus smit dollar nomk egemop</h4><time>01.01.2015</time><p>Utm tellus dolor, dapibus eget, elemen veinki cursu eleifeltas. Aenean auctorbni wisi et urnam. [...] Aliquam at volutpats</p><div class="thumb" role="img" aria-label="Blue financial chart graphic" style="background:linear-gradient(135deg,#0b2a5a,#2f7ad0 60%,#0b1f40)"></div></article>
  <article class="post right" style="left:634px;top:98px"><div class="thumb" role="img" aria-label="Hand holding a glowing tablet" style="background:linear-gradient(135deg,#0a1a3a,#3a78c0 50%,#101830)"></div><h4>Ut tellus dolor, dapibus smit dollar nomk egemop</h4><time>01.01.2015</time><p>Utm tellus dolor, dapibus eget, elemen veinki cursu eleifeltas. Aenean auctorbni wisi et urnam. [...] Aliquam at volutpats</p></article>
  <div class="sep" style="left:132px;top:202px;width:446px"></div>
  <div class="sep" style="left:634px;top:202px;width:441px"></div>

  <article class="post left" style="left:132px;top:221px"><h4>Ut tellus dolor, dapibus smit dollar nomk egemop</h4><time>01.01.2015</time><p>Utm tellus dolor, dapibus eget, elemen veinki cursu eleifeltas. Aenean auctorbni wisi et urnam. [...] Aliquam at volutpats</p><div class="thumb" role="img" aria-label="Villa pool with lounge chairs" style="background:linear-gradient(180deg,#6a4a3a,#c09060 45%,#2a8ab8)"></div></article>
  <article class="post right" style="left:634px;top:221px"><div class="thumb" role="img" aria-label="Resort house with pool under blue sky" style="background:linear-gradient(180deg,#4f8ed0,#d8c8a8 50%,#1f8ac8)"></div><h4>Ut tellus dolor, dapibus smit dollar nomk egemop</h4><time>01.01.2015</time><p>Utm tellus dolor, dapibus eget, elemen veinki cursu eleifeltas. Aenean auctorbni wisi et urnam. [...] Aliquam at volutpats</p></article>
  <div class="sep" style="left:132px;top:327px;width:446px"></div>
  <div class="sep" style="left:634px;top:327px;width:441px"></div>

  <article class="post left" style="left:132px;top:346px"><h4>Ut tellus dolor, dapibus smit dollar nomk egemop</h4><time>01.01.2015</time><p>Utm tellus dolor, dapibus eget, elemen veinki cursu eleifeltas. Aenean auctorbni wisi et urnam. [...] Aliquam at volutpats</p><div class="thumb" role="img" aria-label="Interior with blue accent wall" style="background:linear-gradient(135deg,#2a4a8a,#8a7a6a 60%,#3a3028)"></div></article>
  <article class="post right" style="left:634px;top:346px"><div class="thumb" role="img" aria-label="Beachfront home with palm trees" style="background:linear-gradient(180deg,#7aa8d8,#c8b898 50%,#4a6a4a)"></div><h4>Ut tellus dolor, dapibus smit dollar nomk egemop</h4><time>01.01.2015</time><p>Utm tellus dolor, dapibus eget, elemen veinki cursu eleifeltas. Aenean auctorbni wisi et urnam. [...] Aliquam at volutpats</p></article>
</section>

<section class="team">
  <h2>OUT TEAM</h2>
  <svg class="tree" width="1200" height="200" viewBox="0 0 1200 200" fill="none" stroke="#cfcfcf" stroke-width="1.5">
    <path d="M270 109 H592 M608 109 H950"/>
    <circle cx="600" cy="109" r="8"/>
    <path d="M270 109 V171 M500 109 V171 M727 109 V171 M950 109 V171"/>
  </svg>
  <div class="member" style="left:190px;top:168px"><div class="ring" style="width:130px;height:130px"><div class="face" role="img" aria-label="Portrait of a team member" style="width:112px;height:112px"></div></div><b>Lorem ipsum</b></div>
  <div class="member" style="left:420px;top:172px"><div class="ring" style="width:122px;height:122px"><div class="face" role="img" aria-label="Portrait of a team member" style="width:104px;height:104px"></div></div><b>Lorem ipsum</b></div>
  <div class="member" style="left:647px;top:172px"><div class="ring" style="width:122px;height:122px"><div class="face" role="img" aria-label="Portrait of a team member" style="width:104px;height:104px"></div></div><b>Lorem ipsum</b></div>
  <div class="member" style="left:870px;top:172px"><div class="ring" style="width:122px;height:122px"><div class="face" role="img" aria-label="Portrait of a team member" style="width:104px;height:104px"></div></div><b>Lorem ipsum</b></div>

  <blockquote class="quote"><span class="tip"></span><span class="tip2"></span>Lorem ipsum dolor sit amet, consectetuer adipiscing elit, sed diam nonummy nibh euismod tincidunt ut laoreet dolore magna aliquam erat volutpat. Ut wisi enim ad minim veniam, quis nostrud exerci tation ullamcorper suscipit lobortis nisl ut aliquip ex ea commodo consequat. Duis autem vel eum iriure dolor in hendrerit in vulputate velit esse molestie consequat, vel illum dolore eu feugiat nulla facilisis at vero eros et accumsan et iusto odio dignissim qui blandit praesent luptatum zzril delenit augue duis dolore te feugait nulla facilisi.</blockquote>
</section>

<footer class="footer">
  <div class="foot-links">HOME<i></i>ABOUT<i></i>PROPERTY SEARCH<i></i>TEAM<i></i>VIDEOS<i></i>BLOG<i></i>EXPLORE O.C<i></i>CONTACT</div>
  <div class="hr"></div>
  <div class="contact-card"><strong>MARLOW ON THE SHORE</strong>Tidewater Lane no 218<br>Near harbor walk<br>Seacliff - 926510</div>
  <div class="contact-lines">
    <div><svg viewBox="0 0 14 14"><path d="M3 1 L5 1 L6 4 L4.5 5.5 C5.5 7.5 6.5 8.5 8.5 9.5 L10 8 L13 9 L13 11 C13 12 12 13 11 13 C6 13 1 8 1 3 C1 2 2 1 3 1 Z" fill="#ccc"/></svg>(949) 555-0142</div>
    <div><svg viewBox="0 0 14 14"><path d="M3 1 L5 1 L6 4 L4.5 5.5 C5.5 7.5 6.5 8.5 8.5 9.5 L10 8 L13 9 L13 11 C13 12 12 13 11 13 C6 13 1 8 1 3 C1 2 2 1 3 1 Z" fill="#ccc"/></svg>(949) 555-0143</div>
    <div><svg viewBox="0 0 14 14"><rect x="1" y="3" width="12" height="8" fill="#ccc"/><path d="M1 3 L7 8 L13 3" stroke="#222" fill="none"/></svg>info@marlowshore.example</div>
  </div>
  <div class="signup-field">Enter Your Email Here</div>
  <div class="signup-btn">SUBMIT</div>
  <div class="brand-box"><span class="b1">MARLOW</span><span class="b2">ON THE SHORE</span></div>
</footer>

<div class="legal">
  <p>© 2015 Marlow on the Shore. All Rights Reserved.</p>
  <div class="social" aria-label="Social links"><span></span><span></span><span></span><span></span></div>
</div>

</body>
</html>
```